Update our business cards to match our awesome new website

Need a new design for company business cards. We have recently revamped our website and would like our business cards to get a refresh too. I've uploaded the company artwork, logo, as well as the Branding Deck to better understand the look & feel of our brand. Please visit the website at hollowbrookestatesmi.com.

Industry/Entity Type

Real Estate

Contact Information for Business Card

must use the colors outlined in the Branding Deck uploaded to the site, or the colors of our logo.

Font styles to use
Other font styles liked:
• Calibri

Requirements
Must have
• Required items: Name, title, company logo, address: 218 Fenwick St. Suite 300, Maple Ridge, OH 44873, email address: cole@hollowbrookestatesMI.com, company phone 800-555-0193, cell: 248-555-0162
Nice to have
• a more simple design. not complicated
Should not have
• cartoonish characters, or whimsical writing or artwork, stay within our branding colors

```html
<!DOCTYPE html>
<html lang="en">
<head>
<meta charset="utf-8">
<title>Hollowbrook Estates – Business Card</title>
<link href="https://fonts.googleapis.com/css2?family=Carlito:wght@400;700&display=swap" rel="stylesheet">
<style>
  :root {
    --bg: #e4e6e8;
    --card: #ffffff;
    --ink: #1c1c1c;
    --green-light: #9cc94a;
    --green-mid: #7cb342;
    --green: #4f9a45;
    --green-dark: #3b7d37;
    --green-arc: #7cc142;
    --green-name: #3f8f3a;
    --green-text: #6cae2e;
    --accent: #f08a24;
  }
  * { box-sizing: border-box; margin: 0; padding: 0; }
  html, body { width: 1200px; height: 965px; overflow: hidden; }
  body {
    background: var(--bg);
    font-family: "Carlito", "Calibri", sans-serif;
    position: relative;
  }
  .card {
    position: absolute;
    width: 640px;
    height: 366px;
    background: var(--card);
    border-radius: 26px;
    overflow: hidden;
    box-shadow: 0 10px 30px rgba(0,0,0,.18);
  }
  .card-front { left: 60px; top: 70px; }
  .card-back { left: 500px; top: 520px; }
  .card svg.decor { position: absolute; inset: 0; width: 100%; height: 100%; }

  .wordmark { position: absolute; color: var(--ink); font-weight: 400; line-height: 1; z-index: 1; }
  .wordmark .name { display: block; text-transform: uppercase; letter-spacing: .5px; white-space: nowrap; }
  .wordmark .sub { display: block; text-align: right; font-size: 11px; margin-top: 4px; }
  .card-front .wordmark { left: 0; right: 0; top: 96px; text-align: center; }
  .card-front .wordmark .name { font-size: 36px; }
  .card-front .wordmark .inner { display: inline-block; }

  .card-back .wordmark { left: 34px; top: 34px; }
  .card-back .wordmark .name { font-size: 28px; }

  .person { position: absolute; left: 34px; top: 112px; }
  .person-name { color: var(--green-name); font-weight: 700; font-size: 26px; text-transform: uppercase; letter-spacing: .5px; line-height: 1; }
  .person-title { color: var(--green-text); font-size: 16px; margin-top: 4px; }

  .contacts { position: absolute; left: 34px; top: 182px; list-style: none; }
  .contacts li { display: flex; align-items: center; gap: 10px; color: var(--green-name); font-size: 16px; line-height: 24px; }
  .contacts svg { width: 16px; height: 16px; flex: none; }

  .address { position: absolute; left: 34px; top: 290px; color: var(--green-text); font-size: 16px; line-height: 20px; font-style: normal; }
  .address::before { content: ""; display: block; width: 18px; height: 2px; background: var(--accent); margin-bottom: 8px; }
</style>
</head>
<body>

<section class="card card-front">
  <svg class="decor" viewBox="0 0 640 366" preserveAspectRatio="none" aria-hidden="true">
    <path d="M0 240 C200 175 420 125 640 112 L640 366 L0 366 Z" fill="var(--green-light)"/>
    <path d="M0 280 C220 215 440 185 640 190 L640 366 L0 366 Z" fill="var(--green-mid)"/>
    <path d="M0 318 C240 262 460 245 640 250 L640 366 L0 366 Z" fill="var(--green)"/>
    <path d="M0 350 C260 318 460 300 640 296 L640 366 L0 366 Z" fill="var(--green-dark)"/>
  </svg>
  <div class="wordmark">
    <div class="inner">
      <span class="name">Hollowbrook Estates</span>
      <span class="sub">of Michigan, LLC</span>
    </div>
  </div>
</section>

<section class="card card-back">
  <svg class="decor" viewBox="0 0 640 366" preserveAspectRatio="none" aria-hidden="true">
    <path d="M395 0 C500 30 560 90 560 190 C545 110 500 45 420 0 Z" fill="var(--green-arc)"/>
    <path d="M640 40 C615 190 560 300 440 366 L640 366 Z" fill="var(--green)"/>
    <path d="M628 110 C620 160 606 205 588 250" stroke="#fff" stroke-width="5" fill="none" stroke-linecap="round"/>
  </svg>

  <div class="wordmark">
    <span class="name">Hollowbrook Estates</span>
    <span class="sub">of Michigan, LLC</span>
  </div>

  <div class="person">
    <div class="person-name">Cole Whitaker</div>
    <div class="person-title">Administrator</div>
  </div>

  <ul class="contacts">
    <li>
      <svg viewBox="0 0 16 16" aria-hidden="true"><path d="M4 1.5 L6.5 4 L5 6 C6 8 8 10 10 11 L12 9.5 L14.5 12 L12.5 14.5 C7 14 2 9 1.5 3.5 Z" fill="none" stroke="var(--green-text)" stroke-width="1.3" stroke-linejoin="round"/></svg>
      800-555-0193
    </li>
    <li>
      <svg viewBox="0 0 16 16" aria-hidden="true"><rect x="4" y="1" width="8" height="14" rx="1.5" fill="none" stroke="var(--green-text)" stroke-width="1.3"/><line x1="7" y1="12.5" x2="9" y2="12.5" stroke="var(--green-text)" stroke-width="1.3"/></svg>
      248-555-0162
    </li>
    <li>
      <svg viewBox="0 0 16 16" aria-hidden="true"><rect x="1" y="3.5" width="14" height="9" fill="none" stroke="var(--green-text)" stroke-width="1.3"/><path d="M1 3.5 L8 9 L15 3.5" fill="none" stroke="var(--green-text)" stroke-width="1.3"/></svg>
      cole@hollowbrookestatesMI.com
    </li>
    <li>
      <svg viewBox="0 0 16 16" aria-hidden="true"><circle cx="8" cy="8" r="6.5" fill="none" stroke="var(--green-text)" stroke-width="1.3"/><ellipse cx="8" cy="8" rx="3" ry="6.5" fill="none" stroke="var(--green-text)" stroke-width="1.1"/><line x1="1.5" y1="8" x2="14.5" y2="8" stroke="var(--green-text)" stroke-width="1.1"/></svg>
      www.hollowbrookestatesmi.com
    </li>
  </ul>

  <address class="address">
    218 Fenwick St. Suite 300<br>
    Maple Ridge, OH 44873
  </address>
</section>

</body>
</html>
```